Travel Itinerary Planning Website Redesign

We have built our own website for a travel itinerary planning service using Wix but are not professional designers. We need help getting over the finish line with a redesign of our website. <br/><br/>We like material design elements, icons and styling. The pages need to flow well one to another and evoke a sense of exclusivity, without giving the impression that it's unattainable. The website doesn't need to keep its current "boxy" format but instead should have a better aesthetic and flow. We're also looking for a complete redesign of the "How It Works" section (shown on two different pages of the website) to be more visually pleasing and easy to understand (maybe using icons or infographic style people). <br/><br/>We already have our logo and selected colors. The copy is also available on the live site as well. The redesign will focus on 4 pages: the homepage and the three service pages (one page per service). The website is currently live at www.trelmavista.com. Fonts should be Helvetica Bold, Regular and Light. Preferred color scheme is attached.

Target Market(s)

Ages 28-65, living in the US, mostly large cities with a desire for well planned, non-group travels

Industry/Entity Type

Travel Industry

Font styles to use
Other font styles liked:
• Helvetica

Colors

Designer to choose colors to be used in the design.

Requirements
Must have
• Make sure to use colors we provided in the attachment and what's on the current website
• Redesign "How it Works"
• Include ambassadors area
• Have a second page that showcases how the "Personal Trip Planning" page should look
Should not have
• No header menu needed for this project

```html
<!DOCTYPE html>
<html lang="en">
<head>
<meta charset="utf-8">
<title>Trelmavista – VIP Trip Planning</title>
<link href="https://fonts.googleapis.com/css2?family=Poppins:wght@300;400;600;700&family=Open+Sans:wght@300;400;600&display=swap" rel="stylesheet">
<style>
  :root{
    --orange:#f9bd68;
    --orange-soft:#fbc978;
    --gold:#b8873c;
    --gold-dark:#8d6426;
    --cream:#fdf2e1;
    --ink:#2f2f2f;
    --muted:#5d5d5d;
    --white:#ffffff;
    --footer:#262626;
    --footer-deep:#1c1c1c;
    --grey-card:#f1f1f1;
  }
  *{box-sizing:border-box;margin:0;padding:0}
  html,body{width:1200px;height:4700px;overflow:hidden}
  body{position:relative;background:var(--white);font-family:"Open Sans",Arial,sans-serif;color:var(--ink)}
  h1,h2,h3,h4,.btn,.brand{font-family:"Poppins",Arial,sans-serif}
  .btn{display:inline-block;background:var(--gold);color:var(--white);font-weight:600;font-size:20px;letter-spacing:1px;padding:14px 30px;text-transform:uppercase}
  .section-title{font-size:34px;font-weight:700;text-align:center;color:var(--ink)}
  .section-title::after{content:"";display:block;width:60px;height:4px;background:var(--gold);margin:14px auto 0}

  /* Hero */
  .hero{position:absolute;left:0;top:0;width:1200px;height:620px;background:linear-gradient(180deg,#6f8da3 0%,#8eaac0 35%,#5f7d93 70%,#3d5566 100%)}
  .hero-photo{position:absolute;inset:0;background:radial-gradient(ellipse at 75% 85%,#2f3b44 0%,rgba(47,59,68,0) 45%)}
  .brand-mark{position:absolute;left:120px;top:20px;display:flex;align-items:center;gap:12px}
  .brand-mark .dot{width:26px;height:26px;border-radius:50%;background:var(--orange)}
  .brand{color:var(--white);font-weight:700;font-size:20px}
  .menu-icon{position:absolute;right:128px;top:28px}
  .hero-copy{position:absolute;left:128px;top:330px;width:620px;color:var(--white)}
  .hero-copy h1{font-size:50px;line-height:1.12;font-weight:700;text-transform:uppercase}
  .hero-copy p{font-size:20px;line-height:1.45;margin:18px 0 30px;width:460px}

  /* Services */
  .service{position:absolute;left:128px;width:940px;height:336px;display:flex}
  .service-card{width:464px;height:100%;background:var(--orange);position:relative}
  .service-label{position:absolute;left:38px;top:50%;transform:translate(-50%,-50%) rotate(-90deg);transform-origin:center;font-family:"Poppins",sans-serif;font-size:26px;font-weight:600;color:var(--gold-dark);white-space:nowrap}
  .service-line{position:absolute;left:36px;width:2px;height:60px;background:var(--gold-dark)}
  .service-body{position:absolute;left:110px;top:50%;transform:translateY(-50%);width:300px;font-size:19px;line-height:1.5;color:var(--ink)}
  .service-body .more{display:inline-block;margin-top:16px;font-size:14px;font-weight:600;color:var(--gold-dark);border-bottom:2px solid var(--gold-dark)}
  .service-photo{flex:1;height:100%}

  /* How it works */
  .how{position:absolute;left:0;top:1740px;width:1200px;height:400px;background:var(--cream);padding-top:50px}
  .steps{display:flex;justify-content:space-between;width:980px;margin:60px auto 0}
  .step{width:170px;text-align:center;font-size:18px;font-weight:600;line-height:1.35}
  .step svg{display:block;margin:0 auto 18px}

  /* Why */
  .why{position:absolute;left:0;top:2180px;width:1200px}
  .why-grid{display:grid;grid-template-columns:460px 460px;column-gap:100px;row-gap:70px;width:1020px;margin:60px auto 0}
  .why-item{display:flex;gap:28px}
  .why-item svg{flex:none}
  .why-item h3{font-size:20px;font-weight:600;line-height:1.3;margin-bottom:10px}
  .why-item p{font-size:17px;line-height:1.5;color:var(--muted)}

  /* Team */
  .team{position:absolute;left:0;top:2740px;width:1200px;height:560px}
  .team-band{position:absolute;left:0;top:190px;width:1200px;height:330px;background:var(--cream)}
  .team-row{position:absolute;left:128px;top:100px;width:940px;display:flex;justify-content:space-between}
  .member{width:290px}
  .member .photo{height:290px}
  .member h4{font-size:20px;font-weight:700;margin-top:22px;text-transform:uppercase}
  .member span{font-size:15px;color:var(--muted)}
  .team .btn{position:absolute;left:50%;transform:translateX(-50%);top:480px;font-size:17px;padding:12px 26px}

  /* Blog */
  .blog{position:absolute;left:0;top:3330px;width:1200px}
  .blog-row{display:flex;width:940px;margin:60px auto 0;height:350px}
  .blog-photo{width:470px;height:100%}
  .blog-card{flex:1;background:var(--grey-card);padding:36px 40px;margin:20px 0}
  .author{display:flex;align-items:center;gap:12px;font-size:14px;color:var(--muted)}
  .author .avatar{width:34px;height:34px;border-radius:50%;background:#9aa48a}
  .author small{display:block;font-size:12px}
  .blog-card h3{font-size:26px;font-weight:600;margin:26px 0 14px}
  .blog-card p{font-size:15px;line-height:1.55;color:var(--muted)}

  /* CTA */
  .cta{position:absolute;left:0;top:3860px;width:1200px;height:420px}
  .cta-photo{position:absolute;left:0;top:60px;width:800px;height:340px}
  .cta-card{position:absolute;left:610px;top:0;width:460px;height:360px;background:var(--orange);padding:76px 0 0 110px}
  .cta-card h2{font-size:38px;font-weight:600;line-height:1.2;color:var(--ink)}
  .cta-card .btn{margin-top:40px;font-size:18px;padding:12px 28px}

  /* Footer */
  .footer{position:absolute;left:0;top:4300px;width:1200px;height:400px;background:var(--footer);color:#d8d8d8;font-size:14px}
  .footer-cols{display:flex;width:940px;margin:0 auto;padding-top:44px;gap:60px}
  .col-about{width:310px;line-height:1.55}
  .col-about .contact{display:flex;align-items:center;gap:12px;margin-top:24px;font-weight:600;font-size:13px;letter-spacing:.5px;text-transform:uppercase}
  .footer h4{font-size:13px;font-weight:600;color:var(--white);margin-bottom:16px;text-transform:uppercase;letter-spacing:.5px}
  .col-links{width:200px}
  .col-links li{list-style:none;line-height:1.9;font-size:13px}
  .col-form{flex:1}
  .col-form label{display:block;font-size:12px;margin-bottom:4px}
  .col-form .field{background:var(--white);height:28px;margin-bottom:10px}
  .col-form .field.tall{height:66px}
  .col-form .btn{font-size:14px;padding:9px 20px}
  .copyright{position:absolute;left:0;bottom:0;width:1200px;height:40px;background:var(--footer-deep);text-align:center;line-height:40px;font-size:12px;color:#a9a9a9}
</style>
</head>
<body>

<header class="hero">
  <div class="hero-photo" role="img" aria-label="Hiker with a backpack standing on a rocky peak above misty blue mountains"></div>
  <div class="brand-mark"><span class="dot"></span><span class="brand">Trelmavista</span></div>
  <svg class="menu-icon" width="30" height="22" viewBox="0 0 30 22" aria-label="Menu"><g fill="#fff"><rect width="30" height="3"/><rect y="9" width="30" height="3"/><rect y="18" width="30" height="3"/></g></svg>
  <div class="hero-copy">
    <h1>VIP Trip Planning Services for Every Budget</h1>
    <p>Trelmavista creates template-free, handcrafted travel itineraries just for you.</p>
    <span class="btn">Get Started</span>
  </div>
</header>

<section class="service" style="top:664px">
  <div class="service-card">
    <span class="service-label">Personal Trip</span>
    <span class="service-line" style="top:250px"></span>
    <div class="service-body">Get your personalized itinerary from an expert travel engineer and access it anywhere.<br><span class="more">Learn More</span></div>
  </div>
  <div class="service-photo" role="img" aria-label="Smiling woman leading a traveler by the hand" style="background:linear-gradient(135deg,#c9b59a,#8a7a66 60%,#d9cfc3)"></div>
</section>
<section class="service" style="top:1000px">
  <div class="service-card">
    <span class="service-label">Business Trip</span>
    <span class="service-line" style="top:250px"></span>
    <div class="service-body">Get a tailored sightseeing itinerary while on the go for business.<br><span class="more">Learn More</span></div>
  </div>
  <div class="service-photo" role="img" aria-label="Business travelers with luggage walking through an airport terminal" style="background:linear-gradient(180deg,#c8cfd6,#9aa3ab 55%,#6d737a)"></div>
</section>
<section class="service" style="top:1336px">
  <div class="service-card">
    <span class="service-label">Overseas Event</span>
    <span class="service-line" style="top:260px"></span>
    <div class="service-body">Get recommendations and logistics guidance for your overseas events.<br><span class="more">Learn More</span></div>
  </div>
  <div class="service-photo" role="img" aria-label="Hot air balloons rising over a rocky valley at sunrise" style="background:linear-gradient(180deg,#7fa9d6,#b7cbe0 50%,#9a7f62)"></div>
</section>

<section class="how">
  <h2 class="section-title">How it Works</h2>
  <div class="steps">
    <div class="step">
      <svg width="60" height="64" viewBox="0 0 60 64" fill="none" stroke="#b8873c" stroke-width="3"><rect x="10" y="8" width="40" height="52" rx="3"/><rect x="22" y="3" width="16" height="9" rx="2"/><path d="M18 26h24M18 36h24M18 46h16"/></svg>
      Select<br>The Service
    </div>
    <div class="step">
      <svg width="64" height="64" viewBox="0 0 64 64" fill="none" stroke="#b8873c" stroke-width="3"><rect x="6" y="6" width="38" height="52" rx="3"/><path d="M14 20h22M14 30h22M14 40h12"/><path d="M56 14l-20 30-4 8 8-4 20-30z"/></svg>
      Complete<br>the Survey
    </div>
    <div class="step">
      <svg width="50" height="64" viewBox="0 0 50 64" fill="none" stroke="#b8873c" stroke-width="3"><rect x="8" y="18" width="34" height="38" rx="4"/><path d="M18 18V6h14v12M16 56v5M34 56v5M18 30v16M32 30v16"/></svg>
      Connect with a<br>Travel Engineer
    </div>
    <div class="step">
      <svg width="70" height="64" viewBox="0 0 70 64" fill="none" stroke="#b8873c" stroke-width="3"><path d="M4 14l20-8 22 8 20-8v44l-20 8-22-8-20 8z"/><path d="M24 6v44M46 14v44"/><circle cx="35" cy="30" r="5"/></svg>
      Access<br>Custom Itinerary
    </div>
    <div class="step">
      <svg width="64" height="64" viewBox="0 0 64 64" fill="none" stroke="#b8873c" stroke-width="3"><path d="M6 36l52-22-14 40-12-14-12 6z"/><path d="M32 40l26-26"/></svg>
      Travel<br>Worry-Free
    </div>
  </div>
</section>

<section class="why">
  <h2 class="section-title">Why Trelmavista</h2>
  <div class="why-grid">
    <div class="why-item">
      <svg width="64" height="64" viewBox="0 0 64 64" fill="none" stroke="#b8873c" stroke-width="3"><circle cx="32" cy="30" r="18"/><path d="M32 20l3 7h7l-6 4 2 7-6-4-6 4 2-7-6-4h7z" fill="#b8873c"/><path d="M10 40c4 12 14 18 22 18s18-6 22-18"/></svg>
      <div><h3>5-Star Travel Planning<br>for Every Budget</h3><p>While glove service and exceptional travel planning is our motto.</p></div>
    </div>
    <div class="why-item">
      <svg width="64" height="64" viewBox="0 0 64 64" fill="none" stroke="#b8873c" stroke-width="3"><rect x="14" y="6" width="34" height="48" rx="2"/><path d="M22 18h18M22 28h18M22 38h10"/><rect x="36" y="36" width="20" height="20" rx="2" fill="#b8873c"/></svg>
      <div><h3>A Travel Itinerary<br>Engineered Just For You</h3><p>Trelmavista caters to all needs. Going points? Lounge access? No problem. We mastered the art of optimizing miles.</p></div>
    </div>
    <div class="why-item">
      <svg width="64" height="64" viewBox="0 0 64 64" fill="none" stroke="#b8873c" stroke-width="3"><rect x="8" y="8" width="34" height="46" rx="2"/><path d="M16 20h18M16 30h18M16 40h10"/><circle cx="46" cy="44" r="10" fill="#b8873c" stroke="none"/><path d="M41 44h10M46 39v10" stroke="#fff"/></svg>
      <div><h3>Avoid Common<br>Traveler Mistakes</h3><p>While planning or vacationing, it is easy to make costly mistakes. Let us remove that worry!</p></div>
    </div>
    <div class="why-item">
      <svg width="64" height="64" viewBox="0 0 64 64" fill="none" stroke="#b8873c" stroke-width="3"><circle cx="32" cy="34" r="22" stroke-dasharray="8 5"/><path d="M32 20v14l10 6"/></svg>
      <div><h3>Save Time and Money</h3><p>A sound travel itinerary takes dedication &amp; commitment, qualities that we provide for each handcrafted journey.</p></div>
    </div>
  </div>
</section>

<section class="team">
  <div class="team-band"></div>
  <h2 class="section-title" style="position:absolute;left:0;top:0;width:1200px">Our Team</h2>
  <div class="team-row">
    <div class="member">
      <div class="photo" role="img" aria-label="Portrait of a smiling travel author against a blue sky" style="background:linear-gradient(160deg,#8fb6d8,#c9b4a0 70%,#6b7a86)"></div>
      <h4>Alder Brennick</h4><span>Author &amp; TV Personality</span>
    </div>
    <div class="member">
      <div class="photo" role="img" aria-label="Portrait of a lifestyle influencer holding a camera" style="background:linear-gradient(160deg,#ede5de,#b58a78 60%,#3b2a24)"></div>
      <h4>Selene Varo</h4><span>French Lifestyle Influencer</span>
    </div>
    <div class="member">
      <div class="photo" role="img" aria-label="Portrait of the company founder in a dark jacket" style="background:linear-gradient(160deg,#e8e8e8,#b79c86 55%,#2c2f36)"></div>
      <h4>Matthis Delrue</h4><span>Founder &amp; CEO</span>
    </div>
  </div>
  <span class="btn">More About Us</span>
</section>

<section class="blog">
  <h2 class="section-title">Latest Blog</h2>
  <div class="blog-row">
    <div class="blog-photo" role="img" aria-label="Path through rows of red torii gates at a Japanese shrine" style="background:linear-gradient(180deg,#8a2b16,#c9471f 45%,#6b2512)"></div>
    <div class="blog-card">
      <div class="author"><span class="avatar"></span><div>Matthis Delrue<small>Jan 16 · 16 min read</small></div></div>
      <h3>2020 Japan Travel Guide</h3>
      <p>Japan, the land of the rising sun and robotics! After a truly exceptional destination, I must be honest, Japan was not in my top 10 countries to visit, but after experiencing the beauty, peacefulness and excitement from our Nippon adventure, I can say with conviction that Japan deserves a spot in everyone's must-see list!</p>
    </div>
  </div>
</section>

<section class="cta">
  <div class="cta-photo" role="img" aria-label="Pyramids rising from golden desert sand under a warm sky" style="background:linear-gradient(180deg,#e9c98f,#d9a45c 50%,#b98447)"></div>
  <div class="cta-card">
    <h2>Ready to<br>Get Planning?</h2>
    <span class="btn">View Services</span>
  </div>
</section>

<footer class="footer">
  <div class="footer-cols">
    <div class="col-about">
      <p>Trelmavista's mission is to engineer personalized, handcrafted travel itineraries and travel plans for travelers worldwide.</p>
      <div class="contact"><svg width="20" height="16" viewBox="0 0 20 16" fill="none" stroke="#f9bd68" stroke-width="2"><rect x="1" y="1" width="18" height="14"/><path d="M1 1l9 8 9-8"/></svg>Questions? Contact us</div>
      <div class="contact"><svg width="18" height="18" viewBox="0 0 18 18"><rect width="18" height="18" rx="3" fill="#f9bd68"/></svg>Follow us on Picterra</div>
    </div>
    <div class="col-links">
      <h4>About Trelmavista</h4>
      <ul>
        <li>Personal Trip Planning</li>
        <li>Business Trip Planning</li>
        <li>Overseas Event Planning</li>
        <li>Free Travel Resources</li>
        <li>Terms and Conditions</li>
        <li>Privacy Policy</li>
      </ul>
    </div>
    <div class="col-form">
      <h4>Contact Us</h4>
      <label>First Name</label><div class="field"></div>
      <label>Email</label><div class="field"></div>
      <label>Your Message</label><div class="field tall"></div>
      <span class="btn">Submit</span>
    </div>
  </div>
  <div class="copyright">Copyright © 2020 All Rights Reserved</div>
</footer>

</body>
</html>
```